Business card and company logo design needed

Need a business card and company logo design for all stationary for an Aviation refueling consultancy business. Our business offers consulting services in the specialist aviation refueling industry. Services range from engineering, compliance and management consultancy through to project management services. This encompasses infrastructure from refinery through to airport and into the aircraft wing.

Design should be simple, 'less-is-more' concept, possibly taking advantage of the 'm' for tevlon and the fact is it the aviation industry. It should convey confidence, safety, experience, professionalism, aviation, engineering?, and should not be afraid to be simple in color...though please do not let this restrict your designs and imagination.

Target Market(s)

Airport authorities, oil majors, aircraft operators

Industry/Entity Type

Airport

Contact Information for Business Card

Tevlon Skyward Advisory Pty Ltd
Darius Tevlon
Director
mobile:+61427305158
email: darius@tevlonadvisory.example
Skype: darius.tevlonadvisory

Logo styles of interest
Emblem Logo
Pictorial/Combination Logo
Abstract Logo
Wordmark Logo
Lettermark Logo
Requirements
Must have
• - A feel of safety, security and confidence
Nice to have
• - Aviation has both heritage and modern 'sexy' elements so would be nice to try and capture both
- Aviation 'JET' fuel color is designated as black in signage or labels
- Themes? : Aviation fuel is derived from oil, it burns, safety, Jet fuel is colorless
- Company is global in reach, borderless like aircraft
Should not have
• - Cliche:

```html
<!DOCTYPE html>
<html lang="en">
<head>
<meta charset="utf-8">
<title>Tevlon Skyward Advisory – Business Card</title>
<link href="https://fonts.googleapis.com/css2?family=Open+Sans:wght@400;600&display=swap" rel="stylesheet">
<style>
  :root{
    --stage:#d9d6d2;
    --card-white:#fbfbfb;
    --card-black:#1d1e20;
    --band-black:#121314;
    --sky-blue:#3b9bd8;
    --ink:#2b2b2b;
    --ink-soft:#6b6b6b;
    --white:#ffffff;
  }
  *{box-sizing:border-box;margin:0;padding:0}
  html,body{width:1200px;height:800px;overflow:hidden}
  body{
    background:var(--stage);
    font-family:"Open Sans",Arial,sans-serif;
    position:relative;
  }
  .card{
    position:absolute;
    top:240px;
    width:560px;height:320px;
    overflow:hidden;
    box-shadow:0 6px 18px rgba(0,0,0,.18);
  }
  .card--front{left:26px;background:var(--card-white)}
  .card--back{left:614px;background:var(--card-black)}

  /* wordmark */
  .wordmark{
    display:flex;align-items:center;gap:10px;
    color:var(--sky-blue);font-weight:600;
    text-transform:uppercase;letter-spacing:2px;line-height:1.15;
  }
  .wordmark__dot{
    flex:none;border-radius:50%;background:var(--sky-blue);
  }
  .card--front .wordmark{position:absolute;left:120px;top:34px;font-size:17px}
  .card--front .wordmark__dot{width:30px;height:30px}

  .card--back .wordmark{
    position:absolute;left:0;right:0;top:96px;justify-content:center;
    font-size:20px;text-align:left;
  }
  .card--back .wordmark__dot{width:38px;height:38px}

  /* name band */
  .name-band{
    position:absolute;left:0;right:0;top:118px;height:64px;
    background:var(--band-black);
    border-top:3px solid var(--white);
    border-bottom:3px solid var(--white);
    outline:2px solid var(--sky-blue);
    display:flex;align-items:center;justify-content:center;
    color:var(--white);
  }
  .name-band::before,.name-band::after{
    content:"";position:absolute;left:0;right:0;height:2px;background:var(--sky-blue);
  }
  .name-band::before{top:-10px}
  .name-band::after{bottom:-10px}
  .person-name{font-size:24px;font-weight:400}
  .person-name__surname{color:var(--sky-blue)}
  .divider{display:inline-block;width:1.5px;height:26px;background:var(--white);margin:0 10px}
  .person-role{font-size:17px}

  /* contacts */
  .contact-line{
    position:absolute;left:16px;right:16px;top:232px;
    display:flex;align-items:center;justify-content:center;gap:7px;
    font-size:11px;color:var(--ink);white-space:nowrap;
  }
  .contact-item{display:flex;align-items:center;gap:5px}
  .contact-item svg{flex:none}
  .contact-sep{width:1px;height:14px;background:var(--ink-soft)}

  /* back stripe */
  .back-stripe{
    position:absolute;left:0;right:0;bottom:58px;height:22px;background:var(--sky-blue);
  }
</style>
</head>
<body>

<section class="card card--front" aria-label="Business card front">
  <div class="wordmark">
    <span class="wordmark__dot"></span>
    <span>Tevlon Skyward Advisory<br>Pty Ltd</span>
  </div>

  <div class="name-band">
    <span class="person-name">Darius <span class="person-name__surname">Tevlon</span></span>
    <span class="divider"></span>
    <span class="person-role">Director</span>
  </div>

  <div class="contact-line">
    <span class="contact-item">
      <svg width="12" height="9" viewBox="0 0 13 10"><rect x="0.5" y="0.5" width="12" height="9" fill="none" stroke="#3b9bd8"/><path d="M0.5 0.5 L6.5 5.5 L12.5 0.5" fill="none" stroke="#3b9bd8"/></svg>
      darius@tevlonadvisory.example
    </span>
    <span class="contact-sep"></span>
    <span class="contact-item">
      <svg width="11" height="11" viewBox="0 0 12 12"><path d="M2.5 1 L4.5 1 L5 3.5 L3.8 4.5 C4.5 6 6 7.5 7.5 8.2 L8.5 7 L11 7.5 L11 9.5 C11 10.3 10.3 11 9.5 11 C5 11 1 7 1 2.5 C1 1.7 1.7 1 2.5 1 Z" fill="#3b9bd8"/></svg>
      +61427305158
    </span>
    <span class="contact-sep"></span>
    <span class="contact-item">
      <svg width="11" height="11" viewBox="0 0 12 12"><circle cx="6" cy="6" r="5.5" fill="#3b9bd8"/></svg>
      Skype: darius.tevlonadvisory
    </span>
  </div>
</section>

<section class="card card--back" aria-label="Business card back">
  <div class="wordmark">
    <span class="wordmark__dot"></span>
    <span>Tevlon Skyward Advisory<br>Pty Ltd</span>
  </div>
  <div class="back-stripe"></div>
</section>

</body>
</html>
```